Platelet Rich Plasma (PRP) Flyer

Hi,

Looking to spruce up our Platelet Rich Plasma Flyer (see power point attachment). I also included previous flyers as examples on the design style we are looking for.

Quorum is our official font of our logo.
Attached is our logo in EPS format.
Please use the current photos in the power point. If you include photos, please make sure the stock image is free.

Files must be under 5MB. JPEG, PNG, PDF, .ai

Thank you,
Dorian

Target Market(s)

Patients

Industry/Entity Type

Healthcare

Font styles to use
Other font styles liked:
• Quorum

Requirements
Must have
• Emphasis on Platelet Rich Plasma Therapy when they pick up the flyer. The price of $199. FSA/HSA Eligible. The different treatment areas. The three addresses. Best of the best logo can be very small, not as important.
Nice to have
• One or two pictures. Less is more
Should not have
• Long paragraphs, multiple sentences.

```html
<!DOCTYPE html>
<html lang="en">
<head>
<meta charset="utf-8">
<title>Platelet Rich Plasma Therapy Flyer</title>
<link href="https://fonts.googleapis.com/css2?family=Roboto:wght@300;400;500;700&family=Barlow+Semi+Condensed:wght@700&family=Oswald:wght@600&display=swap" rel="stylesheet">
<style>
:root{
  --teal:#52bf9e;
  --orange:#ef8450;
  --peach:#fcc9a6;
  --white:#ffffff;
  --text-dark:#1f2a2a;
  --brand:#ef7a3c;
}
*{margin:0;padding:0;box-sizing:border-box}
html,body{width:848px;height:1200px;overflow:hidden;background:var(--white)}
.flyer{position:relative;width:848px;height:1200px;overflow:hidden;font-family:"Roboto",sans-serif;color:var(--white)}
.backdrop{position:absolute;inset:0}
.brand{position:absolute;top:46px;right:36px;display:flex;align-items:center;gap:12px}
.brand-mark{width:30px;height:30px;border-radius:50%;background:var(--teal)}
.brand-name{font-family:"Barlow Semi Condensed",sans-serif;font-weight:700;font-size:31px;line-height:1;color:var(--brand);letter-spacing:.3px;text-transform:uppercase}
.services{position:absolute;top:130px;right:36px;text-align:center;font-weight:300;font-size:21px;line-height:28px;width:310px}
.services .bar{color:var(--brand)}
.phone{position:absolute;top:186px;right:34px;font-weight:400;font-size:39px;letter-spacing:.5px}
.headline{position:absolute;left:38px;top:384px;font-weight:500;font-size:49px;line-height:60px}
.treating{position:absolute;left:38px;top:530px;font-size:17.5px;line-height:24px;font-weight:400;width:345px}
.intro{position:absolute;right:54px;top:540px;width:400px;text-align:right;color:var(--text-dark)}
.eligible{font-weight:700;font-size:30px;line-height:36px;margin-bottom:26px}
.points{list-style:none;font-size:20px;line-height:30px;font-weight:400}
.points li+li{margin-top:16px}
.availability{position:absolute;right:54px;top:928px;text-align:right;color:var(--text-dark);font-weight:700;font-size:17.5px;line-height:23px}
.price{position:absolute;left:132px;top:869px;width:200px;height:200px;border-radius:50%;display:flex;flex-direction:column;align-items:center;justify-content:center;color:var(--text-dark)}
.price-label{font-size:19px;font-weight:400}
.price-amount{font-family:"Oswald",sans-serif;font-weight:600;font-size:66px;line-height:70px;position:relative;padding-left:14px}
.price-amount sup{font-size:28px;position:absolute;left:-6px;top:4px}
.price-unit{font-size:19px}
.offices{position:absolute;left:0;right:0;top:1106px;display:flex;justify-content:center}
.office{width:268px;text-align:center;font-size:13.5px;line-height:19px;font-weight:300}
.office+.office{border-left:1px solid rgba(255,255,255,.85)}
.office-name{font-weight:700}
</style>
</head>
<body>
<main class="flyer">
  <svg class="backdrop" width="848" height="1200" viewBox="0 0 848 1200">
    <defs>
      <linearGradient id="dark-field" x1="0" y1="0" x2="1" y2="1">
        <stop offset="0" stop-color="#4a5257"/>
        <stop offset="1" stop-color="#1c2226"/>
      </linearGradient>
      <radialGradient id="leg-tones" cx="0.3" cy="0.3" r="0.8">
        <stop offset="0" stop-color="#d26d52"/>
        <stop offset="0.35" stop-color="#a8735e"/>
        <stop offset="0.7" stop-color="#33505d"/>
        <stop offset="1" stop-color="#23333b"/>
      </radialGradient>
      <linearGradient id="lab-tones" x1="0" y1="0" x2="1" y2="1">
        <stop offset="0" stop-color="#e9eef2"/>
        <stop offset="0.5" stop-color="#b7c4cf"/>
        <stop offset="1" stop-color="#5d6f7f"/>
      </linearGradient>
      <linearGradient id="ring-tone" x1="0" y1="0" x2="0" y2="1">
        <stop offset="0" stop-color="#2f3d3b"/>
        <stop offset="1" stop-color="#111a19"/>
      </linearGradient>
    </defs>
    <rect width="848" height="1200" fill="url(#dark-field)"/>
    <g role="img" aria-label="Photo of a man holding his painful knee, highlighted in red">
      <path d="M0,0 H640 C610,250 520,470 330,580 C220,640 100,650 0,630 Z" fill="url(#leg-tones)"/>
    </g>
    <g role="img" aria-label="Photo of gloved hands placing blood sample tubes into a centrifuge">
      <path d="M0,620 C130,648 260,620 400,560 L400,1000 L0,1000 Z" fill="url(#lab-tones)"/>
    </g>
    <path d="M848,318 C600,322 420,440 372,620 C352,700 356,860 372,1000 L848,1000 Z" fill="var(--teal)"/>
    <path d="M0,985 C220,950 520,1010 848,962 L848,1200 L0,1200 Z" fill="var(--orange)"/>
    <circle cx="232" cy="969" r="110" fill="url(#ring-tone)"/>
    <circle cx="232" cy="969" r="97" fill="var(--peach)"/>
  </svg>

  <div class="brand">
    <span class="brand-mark"></span>
    <span class="brand-name">Ridgeview Foot &amp; Ankle</span>
  </div>
  <div class="services">Podiatry <span class="bar">|</span> Foot &amp; Ankle Surgery<br>Sports Medicine <span class="bar">|</span> Wound Care</div>
  <div class="phone">(555) 204 - 0917</div>

  <h1 class="headline">Platelet Rich Plasma<br>Therapy (PRP)</h1>
  <p class="treating">Treating: Plantar Fasciitis | Achilles Tendonitis | Tendon &amp; Ligament Injuries</p>

  <div class="intro">
    <p class="eligible">FSA/HSA Eligible</p>
    <ul class="points">
      <li>Your own platelets, concentrated<br>and injected where it hurts</li>
      <li>Growth factors that speed<br>tissue repair and regeneration</li>
      <li>Stimulates new, healthy cells<br>for natural healing</li>
      <li>Consultation required to qualify</li>
    </ul>
  </div>

  <div class="availability">Same Day | Emergency | Saturday Appointments<br>Our Doctors are on call at the RMC ER 24/7</div>

  <div class="price">
    <span class="price-label">Self pay price:</span>
    <span class="price-amount"><sup>$</sup>199</span>
    <span class="price-unit">per treatment</span>
  </div>

  <footer class="offices">
    <div class="office"><div class="office-name">Northgate Office</div>58 Alder Brook Rd. Ste. 120<br>Northgate, MD 21790</div>
    <div class="office"><div class="office-name">Elmwood Office</div>2715 Kestrel Park Blvd. Ste. 204<br>Elmwood, MD 21795</div>
    <div class="office"><div class="office-name">Brookfield Office</div>406 Wellness Way<br>Brookfield, WV 25490</div>
  </footer>
</main>
</body>
</html>
```